Highly-decorative large Family tree to use instead of modern art prin living/dining room or entrance

I am winding down my family project for the time being and want to have a very nice, decorative and pleasant to look at modern "art" print of it as "end result" of the hard work ... also as something for future generations in years to come? I don't really want another boring design of just a tree or boxes and names but would love to have a print design of the attached family tree that thinks out of the box and adds to our home.

I would love to think of some of the 1950s, 60s 70s abstract work as inspiration. The final print should communicate home, belonging and a connection between past and future. Thanks for thinking out side the box ... please shout if you have any questions...!

Target Market(s)

Family

Font styles to use
Serif
Decorative

Colors

Designer to choose colors to be used in the design.

Requirements
Must have
• Art-print quality, must have the look and feel of an art-print, not a family tree or a chart.
• PLEASE NOTE THAT NAMES ONLY NEED TO BE FILLED IN ONCE FINAL WINNING DESIGN HAS BEEN SELECTED.
Should not have
• Should not look or feel like a chart, or a tree.

```html
<!DOCTYPE html>
<html lang="en">
<head>
<meta charset="utf-8">
<title>Family Constellation Print</title>
<link rel="stylesheet" href="https://fonts.googleapis.com/css2?family=Cinzel:wght@700&display=swap">
<style>
  :root {
    --sun: #ffc400;
    --flame: #ff3317;
    --crimson: #d00026;
    --plum: #8a0047;
    --night: #2c0a22;
    --thread: #ffffff;
    --label: #fff6ee;
  }
  html, body {
    margin: 0;
    padding: 0;
    width: 1200px;
    height: 1200px;
    overflow: hidden;
    background: var(--night);
  }
  .print {
    display: block;
    width: 1200px;
    height: 1200px;
  }
  .wave { filter: drop-shadow(-10px -6px 18px rgba(40,0,20,0.55)); }
  .wave--sun { fill: var(--sun); }
  .wave--flame { fill: var(--flame); }
  .wave--crimson { fill: var(--crimson); }
  .wave--plum { fill: var(--plum); }
  .wave--night { fill: var(--night); }
  .thread {
    fill: none;
    stroke: var(--thread);
    stroke-width: 2.5;
    stroke-dasharray: 6 5;
  }
  .thread-knot { fill: var(--thread); }
  .member-name {
    font-family: "Cinzel", serif;
    font-weight: 700;
    font-size: 27px;
    letter-spacing: 3px;
    fill: var(--label);
    filter: drop-shadow(3px 4px 3px rgba(60,0,20,0.6));
  }
  .portrait { filter: drop-shadow(4px 6px 6px rgba(60,0,20,0.45)); }
</style>
</head>
<body>
<svg class="print" viewBox="0 0 1500 1500" xmlns="http://www.w3.org/2000/svg">
  <defs>
    <radialGradient id="portrait-tone" cx="50%" cy="60%" r="60%">
      <stop offset="0%" stop-color="#eab29a"/>
      <stop offset="70%" stop-color="#c27a55"/>
      <stop offset="100%" stop-color="#5a2410"/>
    </radialGradient>
  </defs>

  <g class="waves">
    <rect class="wave--sun" width="1500" height="1500"/>
    <path class="wave wave--flame" d="M790,0 C610,40 430,50 345,150 C270,250 240,380 0,385 L0,1500 L1500,1500 L1500,0 Z"/>
    <path class="wave wave--crimson" d="M0,742 C260,765 410,640 470,470 C530,320 580,258 710,258 L1180,258 C1350,250 1450,140 1500,35 L1500,1500 L0,1500 Z"/>
    <path class="wave wave--plum" d="M0,1100 C320,1130 720,1160 850,950 C950,790 920,560 980,460 C1050,350 1250,330 1500,440 L1500,1500 L0,1500 Z"/>
    <path class="wave wave--night" d="M750,1500 C850,1360 950,1100 1040,960 C1140,800 1260,755 1500,758 L1500,1500 Z"/>
  </g>

  <g class="threads">
    <path class="thread" d="M312,158 L400,170 L400,292"/>
    <path class="thread" d="M190,305 L150,310"/>
    <path class="thread" d="M100,325 L100,525"/>
    <path class="thread" d="M550,302 L562,392 L768,396 L766,603 L677,614"/>
    <path class="thread" d="M88,715 L98,805 L306,808 L303,1017 L214,1027"/>
    <circle class="thread-knot" cx="312" cy="158" r="7"/>
    <circle class="thread-knot" cx="190" cy="305" r="7"/>
    <circle class="thread-knot" cx="550" cy="302" r="7"/>
    <circle class="thread-knot" cx="677" cy="614" r="7"/>
    <circle class="thread-knot" cx="88" cy="715" r="7"/>
    <circle class="thread-knot" cx="214" cy="1027" r="7"/>
  </g>

  <g class="portraits">
    <circle class="portrait" role="img" aria-label="Portrait illustration of a family member" cx="222" cy="122" r="72" fill="url(#portrait-tone)"/>
    <circle class="portrait" role="img" aria-label="Portrait illustration of a family member" cx="102" cy="205" r="84" fill="url(#portrait-tone)"/>
    <circle class="portrait" role="img" aria-label="Portrait illustration of a family member" cx="470" cy="240" r="64" fill="url(#portrait-tone)"/>
    <circle class="portrait" role="img" aria-label="Portrait illustration of a family member" cx="420" cy="362" r="64" fill="url(#portrait-tone)"/>
    <circle class="portrait" role="img" aria-label="Portrait illustration of a family member" cx="200" cy="535" r="74" fill="url(#portrait-tone)"/>
    <circle class="portrait" role="img" aria-label="Portrait illustration of a family member" cx="88" cy="615" r="68" fill="url(#portrait-tone)"/>
    <circle class="portrait" role="img" aria-label="Portrait illustration of a family member" cx="594" cy="562" r="68" fill="url(#portrait-tone)"/>
  </g>

  <g class="names">
    <text class="member-name" x="307" y="67">NAME</text>
    <text class="member-name" x="48" y="319">NAME</text>
    <text class="member-name" x="542" y="238">NAME</text>
    <text class="member-name" x="358" y="477">NAME</text>
    <text class="member-name" x="173" y="650">NAME</text>
    <text class="member-name" x="103" y="719">NAME</text>
    <text class="member-name" x="542" y="669">NAME</text>
  </g>
</svg>
</body>
</html>
```